improvement on my landing page

We are a fansite platform similar to brindlefold.com, quillmarsh.com , tovarenel.com and gleamwick.com. We are aiming to disrupt this space by a much cheaper and advanced platform to help influencers monetise across different tools.

current lander is https://lumorabey.com/

Looking for a modern, clean, feminine , pink. Current style and other competitors list given feel old and this needs to highlight its a cutting edge product replacing them. Designs I like are www.kelvadrop.app for example.

I need a few elaborations from current site on price differences of competitors, icons and more details on features and several other new sections added. Need a form to capture email , name and phone as this is a coming soon page. Can change later as a signup

attached document is how thee site looks, so need to keep the identity

Target Market(s)

influence's, adult

Font styles to use
Sans Serif

Colors
eea4c8
fefafc
ecdaeb

Requirements
Nice to have
• infographics

```html
<!DOCTYPE html>
<html lang="en">
<head>
<meta charset="utf-8">
<title>Lumorabey – Keep 90% of your earnings</title>
<link rel="stylesheet" href="https://fonts.googleapis.com/css2?family=Rubik:wght@400;500;700&family=Arimo:wght@400;700&display=swap">
<style>
:root{
  --pink:#eea4c8;
  --pink-soft:#ecdaeb;
  --paper:#fefafc;
  --hot:#e6407f;
  --brand:#e8175d;
  --ink:#1d1d1f;
  --body:#3a3a3a;
  --muted:#777;
  --night:#141414;
}
*{box-sizing:border-box;margin:0;padding:0}
html,body{width:1200px;height:4886px;overflow:hidden}
body{position:relative;background:var(--paper);font-family:Arimo,Arial,sans-serif;color:var(--body)}
.abs{position:absolute}
.heading{font-family:Rubik,Arial,sans-serif;font-weight:700;color:var(--ink);letter-spacing:.5px}
.section-title{position:absolute;left:0;width:1200px;text-align:center;font-size:38px}
.rule{position:absolute;left:572px;width:56px;height:4px;background:var(--hot)}
.btn{position:absolute;display:flex;align-items:center;justify-content:center;border-radius:24px;background:var(--pink);color:#fff;font-family:Rubik,Arial,sans-serif;font-weight:500;font-size:14px;letter-spacing:.5px;box-shadow:0 4px 10px rgba(238,164,200,.45)}
.placeholder{position:absolute}

/* header */
.logo{left:80px;top:32px;display:flex;align-items:center;gap:14px;font-family:Rubik,Arial,sans-serif;font-weight:500;font-size:30px;letter-spacing:4px;color:var(--ink)}
.logo-dot{width:30px;height:30px;border-radius:50%;background:var(--brand)}
.menu{left:916px;top:30px;width:32px}
.menu span{display:block;height:4px;background:var(--ink);margin-bottom:6px;border-radius:2px}
.header-cta{left:975px;top:27px;width:128px;height:36px;font-size:13px}

/* hero */
.hero-title{left:80px;top:190px;font-size:42px;line-height:44px}
.hero-text{left:81px;top:340px;width:440px;font-size:15.5px;line-height:24px;color:var(--ink)}
.dots{left:84px;top:512px;display:flex;gap:10px;align-items:center}
.dots i{width:10px;height:10px;border-radius:50%;background:var(--ink)}
.dots i.on{width:20px;height:20px;background:#fff;border:2px solid var(--pink);box-shadow:inset 0 0 0 4px #fff,inset 0 0 0 10px var(--pink)}

/* why */
.why-text{left:232px;top:832px;width:736px;text-align:center;font-size:13.5px;line-height:24px;color:var(--body)}
.feature{position:absolute;width:226px;height:222px;background:#fff;border:1px solid #f2d3e2;box-shadow:0 4px 14px rgba(200,120,160,.25);text-align:center;padding:0 26px}
.feature .icon{width:64px;height:64px;margin:26px auto 14px;border-radius:10px;background:var(--pink-soft)}
.feature h3{font-family:Rubik,Arial,sans-serif;font-weight:500;font-size:15px;color:var(--ink);line-height:20px;margin-bottom:8px;letter-spacing:.3px}
.feature p{font-size:13px;line-height:18px;color:var(--body)}

/* fees */
.fee-hero{left:142px;top:1892px;width:427px;height:332px;border:2px solid #c9a1b3;background:linear-gradient(135deg,#8b7d80,#c9bdbd 55%,#6f6265)}
.fee-brand{position:absolute;left:0;width:100%;top:92px;display:flex;justify-content:center;align-items:center;gap:14px;font-family:Rubik,Arial,sans-serif;font-weight:500;font-size:30px;letter-spacing:4px;color:#fff}
.fee-pct{position:absolute;left:0;width:100%;top:140px;text-align:center;font-family:Rubik,Arial,sans-serif;font-weight:700;font-size:38px;color:var(--pink)}
.fee-card{position:absolute;width:226px;height:156px;background:#fff;border:2px solid #f0bdd5;box-shadow:0 4px 14px rgba(200,120,160,.2);text-align:center}
.fee-card .name{margin-top:36px;font-family:Rubik,Arial,sans-serif;font-size:30px;color:#6d6d6d;font-weight:400}
.fee-card .pct{margin-top:16px;font-family:Rubik,Arial,sans-serif;font-weight:700;font-size:27px;color:var(--pink)}

/* news */
.news{position:absolute;top:2503px;width:283px;height:474px;background:#fff;box-shadow:0 4px 16px rgba(130,170,220,.35)}
.news .photo{height:227px}
.news .body{padding:22px 20px}
.news .date{font-size:13px;color:var(--pink);margin-bottom:12px}
.news h4{font-family:Rubik,Arial,sans-serif;font-weight:500;font-size:13.5px;line-height:23px;color:var(--ink);margin-bottom:10px}
.news p{font-size:13px;line-height:21px;color:var(--body)}
.news .more{position:static;display:inline-flex;margin-top:14px;width:116px;height:32px;border-radius:3px;font-size:11px;box-shadow:none}

/* form */
.form-title{left:136px;top:3118px;font-family:Rubik,Arial,sans-serif;font-weight:500;font-size:40px;color:var(--ink)}
.form-sub{left:137px;top:3174px;font-size:14px;color:var(--body)}
.form-rule{left:136px;top:3206px;width:86px;height:3px;background:var(--pink)}
.form-box{left:136px;top:3242px;width:680px;height:436px;background:#fff;border-left:5px solid var(--pink);border-top:5px solid var(--pink);box-shadow:0 4px 18px rgba(0,0,0,.06)}
.field{position:absolute;height:38px;border:1px solid #d6d6d6;font-size:11px;color:#444;padding:12px 14px;background:#fff}
.register{position:absolute;left:184px;top:3564px;width:574px;height:42px;background:var(--pink);color:#fff;font-size:15px;letter-spacing:1px;display:flex;align-items:center;justify-content:center}
.legal{left:184px;top:3624px;font-size:14px;color:var(--body)}

/* testimonials */
.testimonials{left:0;top:3886px;width:1200px;height:560px;background:linear-gradient(180deg,#e6407f,#ec5a92)}
.testimonials .section-title{color:#fff;top:82px}
.testimonials .rule{background:#fff;top:142px}
.quote{position:absolute;left:512px;top:222px;width:468px;font-size:13px;line-height:22px;color:#fff}
.author{position:absolute;left:512px;top:360px;color:#fff;font-size:14px}
.stars{position:absolute;left:512px;top:386px;color:#fff;font-size:15px;letter-spacing:1px}
.qmark{position:absolute;font-family:Georgia,serif;font-size:90px;color:#fff;line-height:1}

/* footer */
.footer{left:0;top:4446px;width:1200px;height:440px;background:var(--night);color:#fff}
.sub-title{position:absolute;top:56px;left:0;width:1200px;text-align:center;font-family:Rubik,Arial,sans-serif;font-weight:500;font-size:24px;line-height:30px}
.sub-input{position:absolute;left:343px;top:127px;width:336px;height:38px;background:#fff;color:#333;font-size:12px;padding:12px 16px}
.sub-btn{position:absolute;left:696px;top:127px;width:159px;height:38px;background:var(--pink);color:#fff;font-size:13px;font-weight:700;display:flex;align-items:center;justify-content:center;letter-spacing:.5px}
.foot-line{position:absolute;left:142px;top:214px;width:910px;height:1px;background:#3a3a3a}
.foot-links{position:absolute;top:268px;left:0;width:1200px;text-align:center;font-size:12.5px;font-weight:700;letter-spacing:.5px}
.foot-links span{margin:0 22px}
.copy{position:absolute;top:306px;left:0;width:1200px;text-align:center;font-size:14px}
.social{position:absolute;top:346px;left:526px;display:flex;gap:10px}
.social i{width:30px;height:30px;border-radius:50%;border:2px solid #fff;display:block}
</style>
</head>
<body>

<!-- background shapes -->
<svg class="abs" style="left:0;top:0" width="1200" height="2300" aria-hidden="true">
  <rect width="1200" height="790" fill="#f7f3f5"/>
  <polygon points="0,830 560,1060 0,1820" fill="#fbe3ee"/>
  <polygon points="1200,1300 620,1700 1200,2300" fill="#fbe3ee"/>
  <polygon points="1200,790 860,790 1200,1040" fill="#fdeef5"/>
</svg>

<!-- header -->
<div class="abs logo"><span class="logo-dot"></span>LUMORABEY</div>
<div class="abs menu"><span></span><span></span><span></span></div>
<div class="btn header-cta">GET STARTED</div>

<!-- hero -->
<h1 class="abs heading hero-title">KEEP 90% OF YOUR<br>EARNINGS<br>NO HIDDEN FEES.</h1>
<p class="abs hero-text">Make more with added revenue streams and features for FREE. Maximise you're your fanbase profits with Lumorabey. (edited)</p>
<div class="btn" style="left:82px;top:440px;width:165px;height:42px">GET STARTED</div>
<div class="btn" style="left:260px;top:440px;width:148px;height:42px">LEAR MORE</div>
<div class="abs dots"><i></i><i class="on"></i><i></i><i></i></div>
<div class="placeholder" role="img" aria-label="Smiling creator with glasses working on a laptop, framed by a soft pink blob shape" style="left:563px;top:88px;width:555px;height:594px;border-radius:46% 54% 44% 56% / 40% 45% 55% 60%;background:linear-gradient(160deg,#f7c7dc,#e9a0c1 60%,#f2b6d1)"></div>

<!-- why choose us -->
<h2 class="heading section-title" style="top:742px">WHY CHOOSE US?</h2>
<div class="rule" style="top:804px"></div>
<p class="abs why-text">Lumorabey was developed to democratise the fan platform space. As entrepreurs ourselves we don't see why you should you be handing over a high percentage of your hard earned profits to platforms with mediocre features and services. Receive 90% of your earnings, with no hidden fees or extras AND with fastest payouts. Monetize with monthly subscriptions through private profile feeds and premium social media accounts. Private messaging and tipping, premium videos and much more. Start earning more and keeping your profits. (edited)</p>

<div class="feature" style="left:119px;top:1073px"><div class="icon" role="img" aria-label="Payout icon"></div><h3>FASTEST PAYOUTS</h3><p>Get your money in less than 7 days</p></div>
<div class="feature" style="left:364px;top:1073px"><div class="icon" role="img" aria-label="Geo blocking icon"></div><h3>GEO BLOCKING</h3><p>Hide your content from specific countries</p></div>
<div class="feature" style="left:610px;top:1073px"><div class="icon" role="img" aria-label="Copyright protection icon" style="margin-top:18px"></div><h3>COPYRIGHT PROTECTION</h3><p>You own your content. Take it down whenever you want.</p></div>
<div class="feature" style="left:855px;top:1073px"><div class="icon" role="img" aria-label="Subscriptions icon"></div><h3>CUSTOMIZABLE SUBSCRIPTIONS</h3><p>Build your own subscription plan to fit your business.</p></div>

<div class="feature" style="left:119px;top:1321px"><div class="icon" role="img" aria-label="Tips icon"></div><h3>TIPS</h3><p>Increase your revenue streams without lifting a finger</p></div>
<div class="feature" style="left:364px;top:1321px"><div class="icon" role="img" aria-label="Private messaging app icon"></div><h3>PRIVATE SNAPLET</h3><p>Easily sell private snaplet access and monitor subscriptions</p></div>
<div class="feature" style="left:610px;top:1321px"><div class="icon" role="img" aria-label="Business data icon"></div><h3>INTELLIGENT BUSINESS DATA</h3><p>Easily monitor your business and learn from intuitive data</p></div>
<div class="feature" style="left:855px;top:1321px"><div class="icon" role="img" aria-label="Private message icon"></div><h3>PRIVATE MESSAGING</h3><p>Engage with your fans on a personal level. Your choice</p></div>

<div class="btn" style="left:489px;top:1619px;width:224px;height:46px">LEAR MORE</div>

<!-- competitor fees -->
<h2 class="heading section-title" style="top:1756px">COMPETITOR FEES</h2>
<div class="rule" style="top:1820px"></div>

<div class="placeholder fee-hero" role="img" aria-label="Muted photo of a creator relaxing in bed">
  <div class="fee-brand"><span class="logo-dot"></span>LUMORABEY</div>
  <div class="fee-pct">10%</div>
  <div class="btn" style="left:100px;top:214px;width:224px;height:44px">START SAVING!</div>
</div>
<div class="fee-card" style="left:607px;top:1892px"><div class="name">Quillmarsh</div><div class="pct">20%</div></div>
<div class="fee-card" style="left:855px;top:1892px"><div class="name">Brindlefold</div><div class="pct">8-15%</div></div>
<div class="fee-card" style="left:607px;top:2069px"><div class="name">Gleamwick</div><div class="pct">25-35%</div></div>
<div class="fee-card" style="left:855px;top:2069px"><div class="name">Tovarenel</div><div class="pct">42.5%</div></div>

<!-- latest news -->
<h2 class="heading section-title" style="top:2373px">LATEST NEWS</h2>
<div class="rule" style="top:2436px"></div>

<article class="news" style="left:146px">
  <div class="photo" role="img" aria-label="Woman with a mug sitting on a blanket" style="background:linear-gradient(135deg,#bfe0ef,#e9dcd6 60%,#a7c6dc)"></div>
  <div class="body"><div class="date">&#9638; FEB 13, 2020</div><h4>NEMO ENIM IPSAM VOLUP QUIA VOLUPTAS SIT</h4><p>Sed ut perspiciatis unde omnis iste natus error sit voluptatem acsntium domque laudantium, totam</p><div class="btn more">LEARN MORE</div></div>
</article>
<article class="news" style="left:459px">
  <div class="photo" role="img" aria-label="Woman posing by a red car at the beach" style="background:linear-gradient(180deg,#5aa5e0,#d8c7b5 60%,#b8393f)"></div>
  <div class="body"><div class="date">&#9638; FEB 13, 2020</div><h4>NEMO ENIM IPSAM VOLUP QUIA VOLUPTAS SIT</h4><p>Sed ut perspiciatis unde omnis iste natus error sit voluptatem acsntium domque laudantium, totam</p><div class="btn more">LEARN MORE</div></div>
</article>
<article class="news" style="left:773px">
  <div class="photo" role="img" aria-label="Woman sitting on a bed in a grey room" style="background:linear-gradient(135deg,#9fa3a7,#d9d6d3 55%,#7f8387)"></div>
  <div class="body"><div class="date">&#9638; FEB 13, 2020</div><h4>NEMO ENIM IPSAM VOLUP QUIA VOLUPTAS SIT</h4><p>Sed ut perspiciatis unde omnis iste natus error sit voluptatem acsntium domque laudantium, totam</p><div class="btn more">LEARN MORE</div></div>
</article>

<!-- signup form -->
<h2 class="abs form-title">Create Your FREE Account</h2>
<p class="abs form-sub">It only takes a few seconds. No credit card required.</p>
<div class="abs form-rule"></div>
<div class="abs form-box"></div>
<div class="field" style="left:184px;top:3290px;width:277px">First Name</div>
<div class="field" style="left:480px;top:3290px;width:278px">Last Name</div>
<div class="field" style="left:184px;top:3346px;width:277px">Phone Number</div>
<div class="field" style="left:480px;top:3346px;width:278px">Email Address</div>
<div class="field" style="left:184px;top:3403px;width:277px">Password</div>
<div class="field" style="left:480px;top:3403px;width:278px">Repeat password</div>
<div class="field" style="left:184px;top:3456px;width:574px;height:86px">Message</div>
<div class="register">REGISTER</div>
<p class="abs legal">Privacy &nbsp;&nbsp;&nbsp;| &nbsp;&nbsp;Terms &amp; Conditions</p>
<div class="placeholder" role="img" aria-label="Smiling woman in a blue dress holding the signup card" style="left:800px;top:3262px;width:262px;height:624px;border-radius:120px 120px 0 0;background:linear-gradient(180deg,#6b4536 0%,#d9a892 28%,#2748a8 48%,#1d3a93 100%)"></div>

<!-- testimonials -->
<section class="abs testimonials">
  <h2 class="heading section-title" style="color:#fff">WHAT OUR CUSTOMERS SAY</h2>
  <div class="rule"></div>
  <svg class="abs" style="left:150px;top:276px" width="26" height="40" aria-hidden="true"><polyline points="20,4 6,20 20,36" fill="none" stroke="#fff" stroke-width="4"/></svg>
  <svg class="abs" style="left:1024px;top:276px" width="26" height="40" aria-hidden="true"><polyline points="6,4 20,20 6,36" fill="none" stroke="#fff" stroke-width="4"/></svg>
  <div class="placeholder" role="img" aria-label="Customer portrait in a sun hat" style="left:227px;top:196px;width:190px;height:190px;border-radius:50%;border:4px solid #fff;background:linear-gradient(160deg,#d9b08c,#8c5a3c)"></div>
  <div class="qmark" style="left:450px;top:200px">&ldquo;</div>
  <p class="quote">Lorem ipsum dolor sit amet, consectetur adipiscing elit, sed do eiusmod tempor incididunt ut labore et dolore magna aliqua. Ut enim ad minim veniam, quis nostrud exercitation ullamco laboris nisi ut aliquip ex ea commodo consequat. Duis aute irure dolor in reprehenderit in voluptate velit esse cillum dolore eu fugiat nulla pariatur. Excepteur sint occaecat cupidatat non proident, sunt in culpa qui officia</p>
  <div class="author">John Doe</div>
  <div class="stars">&#9733;&#9733;&#9733;&#9733;&#9733;</div>
  <div class="qmark" style="left:616px;top:366px">&rdquo;</div>
  <div class="placeholder" role="img" aria-label="City skyline silhouette" style="left:0;top:496px;width:1200px;height:64px;background:#3a1424"></div>
</section>

<!-- footer -->
<footer class="abs footer">
  <h2 class="sub-title">SUBSCRIBE OUR NEWLETTER TO<br>RECEIVE THE LATEST NEWS</h2>
  <div class="sub-input">Enter Your Email</div>
  <div class="sub-btn">SUBSCRIBE</div>
  <div class="foot-line"></div>
  <div class="foot-links"><span>TERMS &amp; CONDITIONS</span>/<span>PRIVACY POLICY</span>/<span>COOKIE POLICY</span>/<span>CONTACT US</span></div>
  <div class="copy">&copy; 2020 LUMORABEY. ALL RIGHTS RESERVED</div>
  <div class="social"><i></i><i></i><i></i><i></i></div>
</footer>

</body>
</html>
```